" A EMPRESA ATUA NO SEGMENTO DE OUTSOURCING DE PRINTIVAÃO: LOCAÇÃO DE IMPRESSORAS E MULTIFUNCIONAIS, E IMPLANTAÇÃO DE SOFTWARES AGREGADOS A ESSAS MÁQUINAS. "

```html
<!DOCTYPE html>
<html lang="pt-BR">
<head>
<meta charset="UTF-8">
<title>Printiva — Cartão de visita</title>
<link rel="stylesheet" href="https://fonts.googleapis.com/css2?family=Saira:wght@400;500&family=Roboto:wght@400&display=swap">
<style>
  :root {
    --navy: #1c2a6b;
    --white: #ffffff;
    --paper: #f4f5f7;
    --backdrop: #e6e7ea;
    --ink: #2a3570;
    --text: #3a3f55;
  }
  * { margin: 0; padding: 0; box-sizing: border-box; }
  html, body { width: 1200px; height: 1200px; overflow: hidden; }
  body {
    background: var(--backdrop);
    font-family: "Roboto", Arial, sans-serif;
    position: relative;
  }
  .card {
    position: absolute;
    left: 150px;
    width: 900px;
    height: 500px;
    overflow: hidden;
    box-shadow: 0 18px 40px rgba(20, 25, 50, 0.18);
  }
  .card--back { top: 80px; background: var(--paper); }
  .card--front { top: 620px; background: var(--navy); }

  .brand { display: flex; flex-direction: column; }
  .brand__name {
    font-family: "Saira", Arial, sans-serif;
    font-weight: 500;
    font-size: 66px;
    letter-spacing: 3px;
    line-height: 1;
  }
  .brand__tagline {
    font-family: "Saira", Arial, sans-serif;
    font-weight: 400;
    font-size: 19px;
    letter-spacing: 2.4px;
    margin-top: 8px;
  }

  .card--front .brand {
    color: var(--white);
    position: absolute;
    left: 50%; top: 50%;
    transform: translate(-50%, -50%);
    align-items: flex-start;
  }

  .card--back .brand {
    color: var(--ink);
    position: absolute;
    left: 60px; top: 70px;
  }
  .card--back .brand__name { font-size: 52px; }
  .card--back .brand__tagline { font-size: 15px; letter-spacing: 1.8px; }

  .back__band {
    position: absolute; top: 0; right: 0;
    width: 200px; height: 100%;
    background: var(--navy);
  }

  .contacts {
    position: absolute;
    left: 420px; bottom: 70px;
    list-style: none;
    display: flex; flex-direction: column; gap: 12px;
    color: var(--text);
    font-size: 15px;
  }
  .contacts__item { display: flex; align-items: flex-start; gap: 12px; }
  .contacts__icon {
    flex: none;
    width: 22px; height: 22px;
    background: var(--navy);
    display: flex; align-items: center; justify-content: center;
  }
  .contacts__icon svg { width: 14px; height: 14px; }
  .contacts__text { line-height: 22px; white-space: nowrap; }
  .contacts__text--address { line-height: 19px; }
</style>
</head>
<body>

  <section class="card card--back" aria-label="Verso do cartão">
    <div class="back__band"></div>

    <div class="brand">
      <span class="brand__name">PRINTIVA</span>
      <span class="brand__tagline">OUTSOURCING DE IMPRESSÃO</span>
    </div>

    <ul class="contacts">
      <li class="contacts__item">
        <span class="contacts__icon">
          <svg viewBox="0 0 24 24" fill="#fff"><path d="M6.6 10.8a15 15 0 0 0 6.6 6.6l2.2-2.2a1 1 0 0 1 1-.25 11.4 11.4 0 0 0 3.6.57 1 1 0 0 1 1 1V20a1 1 0 0 1-1 1A17 17 0 0 1 3 4a1 1 0 0 1 1-1h3.5a1 1 0 0 1 1 1c0 1.25.2 2.45.57 3.57a1 1 0 0 1-.25 1z"/></svg>
        </span>
        <span class="contacts__text">(00) 0000-0000</span>
      </li>
      <li class="contacts__item">
        <span class="contacts__icon">
          <svg viewBox="0 0 24 24" fill="none" stroke="#fff" stroke-width="2.4"><rect x="3" y="5" width="18" height="14"/><path d="M3 6l9 7 9-7"/></svg>
        </span>
        <span class="contacts__text">contato@exemplo.com.br</span>
      </li>
      <li class="contacts__item">
        <span class="contacts__icon">
          <svg viewBox="0 0 24 24" fill="none" stroke="#fff" stroke-width="2.2"><circle cx="12" cy="12" r="9"/><path d="M3 12h18M12 3c3 3 3 15 0 18M12 3c-3 3-3 15 0 18"/></svg>
        </span>
        <span class="contacts__text">www.exemplo.com.br</span>
      </li>
      <li class="contacts__item">
        <span class="contacts__icon">
          <svg viewBox="0 0 24 24" fill="#fff"><path d="M12 2a7 7 0 0 0-7 7c0 5 7 13 7 13s7-8 7-13a7 7 0 0 0-7-7zm0 9.5A2.5 2.5 0 1 1 12 6.5a2.5 2.5 0 0 1 0 5z"/></svg>
        </span>
        <span class="contacts__text contacts__text--address">rua exemplo, nº 000<br>cidade - UF | CEP: 00000-000</span>
      </li>
    </ul>
  </section>

  <section class="card card--front" aria-label="Frente do cartão">
    <div class="brand">
      <span class="brand__name">PRINTIVA</span>
      <span class="brand__tagline">OUTSOURCING DE IMPRESSÃO</span>
    </div>
  </section>

</body>
</html>
```